Corporate business card

Business card design for IT consultancy company.
Clients are larger companies.
Card should have round edges on some or all.
Make the user stop and look at the card.
Steel grey background. But if you have a better idea, show me.
Target Market(s)
Corporate - a but web 2.0
Industry/Entity Type
Business
Contact Information for Business Card
As per design.
Font styles to use
Other font styles liked:
- Helvetica
Colors
5c5c5c
ec2027
ffffff
Requirements
Must have
- Clean design - follow brivo styles
- text in white
- Lets have a conversation in red
- Powered by passion in red
Nice to have
- Uncluttered
Should not have
- Cluttered

```html
<!DOCTYPE html>
<html lang="en">
<head>
<meta charset="utf-8">
<title>Corvane – Business Card</title>
<link href="https://fonts.googleapis.com/css2?family=Arimo:wght@400;700&display=swap" rel="stylesheet">
<style>
  :root {
    --steel: #5c5c5c;
    --red: #ec2027;
    --white: #ffffff;
    --black: #050505;
    --backdrop: #d9d9d9;
    --muted: #d4d4d4;
  }
  * { margin: 0; padding: 0; box-sizing: border-box; }
  html, body { width: 1200px; height: 750px; overflow: hidden; }
  body {
    background: var(--backdrop);
    font-family: "Arimo", Helvetica, Arial, sans-serif;
    display: flex;
    align-items: center;
    justify-content: center;
    gap: 40px;
  }
  .card {
    position: relative;
    width: 540px;
    height: 310px;
    border-radius: 18px;
    overflow: hidden;
    background: linear-gradient(to bottom, var(--white) 0%, #b5b5b5 22%, var(--steel) 42%, #1c1c1c 66%, var(--black) 100%);
    color: var(--white);
  }
  .wordmark {
    position: absolute;
    background: var(--white);
    color: var(--red);
    font-weight: 700;
    letter-spacing: 3px;
    display: flex;
    align-items: center;
    justify-content: center;
  }
  .card--front .wordmark { left: 34px; top: 58px; width: 220px; height: 62px; font-size: 34px; }
  .holder { position: absolute; left: 34px; top: 152px; width: 250px; }
  .holder__name { font-size: 21px; font-weight: 700; letter-spacing: 1.5px; }
  .holder__title { font-size: 11px; letter-spacing: 1.5px; margin-top: 6px; padding-left: 2px; }
  .divider { position: absolute; left: 286px; top: 66px; width: 3px; height: 100px; background: var(--white); }
  .contacts { position: absolute; left: 306px; top: 64px; list-style: none; }
  .contacts li { display: flex; align-items: center; gap: 10px; height: 21px; font-size: 11.5px; color: var(--white); }
  .contacts svg { width: 14px; height: 14px; flex: none; }
  .tagline {
    position: absolute; right: 40px; bottom: 46px;
    color: var(--red); font-size: 12px; font-weight: 700; letter-spacing: 1.5px;
  }
  .card--back .wordmark { left: 120px; top: 118px; width: 300px; height: 72px; font-size: 42px; letter-spacing: 5px; }
  .motto {
    position: absolute; left: 0; right: 0; top: 198px; text-align: center;
    font-size: 19px; font-weight: 700; color: var(--muted);
  }
</style>
</head>
<body>

<section class="card card--front" aria-label="Card front">
  <div class="wordmark">CORVANE</div>
  <div class="holder">
    <div class="holder__name">DANIEL HARTLEY</div>
    <div class="holder__title">MANAGING PARTNER</div>
  </div>
  <div class="divider"></div>
  <ul class="contacts">
    <li><svg viewBox="0 0 16 16" fill="#fff"><path d="M8 1 1 7.5h2V15h4v-4h2v4h4V7.5h2z"/></svg>+61 2 9000 0000</li>
    <li><svg viewBox="0 0 16 16" fill="#fff"><path d="M4 1h3l1 4-2 1.5a9 9 0 0 0 3.5 3.5L11 8l4 1v3a2 2 0 0 1-2 2A12 12 0 0 1 2 3a2 2 0 0 1 2-2z"/></svg>0400 000 000</li>
    <li><svg viewBox="0 0 16 16" fill="none" stroke="#fff" stroke-width="1.5"><rect x="1" y="3" width="14" height="10"/><path d="m1 3 7 6 7-6"/></svg>daniel@corvane.com.au</li>
    <li><svg viewBox="0 0 16 16" fill="#fff"><circle cx="8" cy="8" r="6"/></svg>daniel.hartley</li>
    <li><svg viewBox="0 0 16 16" fill="none" stroke="#fff" stroke-width="1.3"><circle cx="8" cy="8" r="6.5"/><ellipse cx="8" cy="8" rx="3" ry="6.5"/><path d="M1.5 8h13"/></svg>www.corvane.com.au</li>
  </ul>
  <div class="tagline">LET'S TALK IT THROUGH TODAY</div>
</section>

<section class="card card--back" aria-label="Card back">
  <div class="wordmark">CORVANE</div>
  <div class="motto">driven by purpose!</div>
</section>

</body>
</html>
```